The Busy Wren Organic & Natural Soaps is looking for label designs (along with the business card proje

This is my scope and requirements:
Labelling project:
This is related to the Label project I also opened up. (The Busy Wren Organic & Natural Soaps needs a good business card (Contest) )
I have attached an initial draft at a logo I tried to come up with for a business card and labelling/marketing. I am hoping that you can take this logo and 'run with it' to finesse it, make it look unique and professional. If you need to change it, I am open to ideas.
I find that labelling/packaging is hard for me to make it look 'professional' so I am coming to the experts!
I am looking for label designs for 2 different bottles and 2 different bar soaps:
1) Organic Bar Soap (2 possibilities: 1) Kraft 'cigar' band around soap with twine, 2) Kraft soap box with Kraft sticker Labels
2) Natural Olive Oil Based Bar Soap (labelling can be same as Organic but with distinct info)
3) Organic Hand Washes (clear square bottles, 250ml with natural pump)
4) Natural Olive Oil Based Body Wash (taper bottle 200ml with metal silver disc top caps)
I am a start up at home company making Organic and Natural Bar soaps, hand soaps, body washes.
All of my ingredients are organic or natural and will include natural essential oils, exfoliants, natural powders/colours, etc.
Some of the names are: Brisquel (feisty, energetic soap), Dunmoor (more of a sandalwood earthy tones with a sandalwood powder exfoliant), Frosk (maybe changing this name - fresh scented), Plum Cardamom (lemongrass/ginger, exfoliants), etc....
If you need more information, please let me know!
Please find attached: Kraft Paper I am looking at to possibly wrap the Bar Soaps in (I like the different colour concept and am trying to decide between diff colours of Wendell Prask paper to wrap around or plain kraft paper.. whichever the new logo concept will look best with.
The bottles I will be using for the hand soap (250ml square) and the body wash (200ml tapered)
OLD POST:
Hello! I am a start up business that is specializing in making luxury organic bar soaps, natural olive oil bar soaps, organic hand wash, natural olive oil body wash/shower gel that will include essential oils, exfoliants, natural powders, etc. (also accessories: wood soap dishes, etc) .. I am looking for a great designer that can provide me with the business card and labelling designs! I appreciate feedback, ideas on how I can receive a great design to help sell my products!
I am attaching my initial logo design that I would like to keep - but am looking for someone to 'finesse' it or make it more professional/unique looking.
Again, this is hand in hand with the business card project I submitted.
Thanks!
Mirela
Updates
I am sorry for the lack of direction or Scope of the project. I am new at this board.
Labelling project:
I have attached an initial draft at a logo I tried to come up with for a business card and labelling/marketing. I am hoping that you can take this logo and 'run with it' to finesse it, make it look unique and professional.
If you need more information, please let me know.
Hello; I just wanted to let everyone know that if you feel that this brand needs a different logo, I am open to ideas (if you don't think the one I started with is ok). I am coming to the experts here!
Just to confirm also - this is related to the business card project, therefore, there are 2 projects, 2 payments! :)
Cheers

```html
<!DOCTYPE html>
<html lang="en">
<head>
<meta charset="utf-8">
<title>The Busy Wren – Bottle Labels</title>
<link rel="stylesheet" href="https://fonts.googleapis.com/css2?family=Arimo:wght@700&family=Raleway:wght@400&family=Tinos:ital,wght@1,700&display=swap">
<style>
  :root {
    --page: #ffffff;
    --frame: #d4d4d4;
    --kraft: #a38c6c;
    --kraft-edge: #97805f;
    --band: #4a3427;
    --band-text: #ffffff;
    --olive-text: #e6dc7a;
    --olive-outline: #4a3a22;
    --hand-text: #4a3427;
    --hand-outline: #d8c8ac;
  }
  html, body {
    margin: 0;
    padding: 0;
    width: 1200px;
    height: 779px;
    overflow: hidden;
    background: var(--page);
  }
  .canvas {
    position: relative;
    width: 1200px;
    height: 779px;
    box-sizing: border-box;
    border: 2px solid var(--frame);
    background: var(--page);
  }
  .label {
    position: absolute;
    background: var(--kraft);
    box-shadow: inset 0 0 0 1px var(--kraft-edge);
    overflow: hidden;
  }
  .label--rounded { border-radius: 10px; }
  .label--body-wash-wrap { left: 184px; top: 276px; width: 105px; height: 219px; }
  .label--body-wash-flat { left: 364px; top: 276px; width: 118px; height: 268px; }
  .label--hand-wash-wrap { left: 716px; top: 264px; width: 111px; height: 311px; border-radius: 8px; }
  .label--hand-wash-flat { left: 911px; top: 264px; width: 110px; height: 311px; }

  .brand-band {
    position: absolute;
    left: 0;
    right: 0;
    background: var(--band);
    color: var(--band-text);
    font-family: "Raleway", sans-serif;
    text-align: center;
    display: flex;
    flex-direction: column;
    justify-content: center;
  }
  .label--body-wash-wrap .brand-band,
  .label--body-wash-flat .brand-band { top: 48px; height: 56px; }
  .label--hand-wash-wrap .brand-band,
  .label--hand-wash-flat .brand-band { top: 51px; height: 62px; }

  .brand-name {
    font-size: 15px;
    line-height: 1.1;
    letter-spacing: 0.2px;
  }
  .brand-tagline {
    font-size: 6.5px;
    line-height: 1.3;
    margin-top: 2px;
  }

  .product-name {
    position: absolute;
    left: 0;
    right: 0;
    text-align: center;
    font-family: "Arimo", sans-serif;
    font-weight: 700;
    line-height: 1.2;
  }
  .product-name--olive {
    top: 136px;
    font-size: 14px;
    color: var(--olive-text);
    -webkit-text-stroke: 0.6px var(--olive-outline);
    paint-order: stroke fill;
  }
  .product-name--hand {
    top: 150px;
    font-size: 15px;
    line-height: 1.45;
    color: var(--hand-text);
    -webkit-text-stroke: 0.5px var(--hand-outline);
  }
  .product-note {
    position: absolute;
    left: 0;
    right: 0;
    top: 230px;
    text-align: center;
    font-family: "Tinos", serif;
    font-style: italic;
    font-weight: 700;
    font-size: 8px;
    color: var(--hand-text);
  }
</style>
</head>
<body>
<main class="canvas">

  <section class="label label--body-wash-wrap" aria-label="Body wash label, wrap view">
    <div class="brand-band">
      <span class="brand-name">The Busy Wren</span>
      <span class="brand-tagline">Organic &amp; Natural Soaps</span>
    </div>
    <p class="product-name product-name--olive" style="margin:0">Natural<br>Olive Oil<br>Based<br>Body Wash</p>
  </section>

  <section class="label label--rounded label--body-wash-flat" aria-label="Body wash label, flat">
    <div class="brand-band">
      <span class="brand-name">The Busy Wren</span>
      <span class="brand-tagline">Organic &amp; Natural Soaps</span>
    </div>
    <p class="product-name product-name--olive" style="margin:0">Natural<br>Olive Oil<br>Based<br>Body Wash</p>
  </section>

  <section class="label label--hand-wash-wrap" aria-label="Hand wash label, wrap view">
    <div class="brand-band">
      <span class="brand-name">The Busy Wren</span>
      <span class="brand-tagline">Organic &amp; Natural Soaps</span>
    </div>
    <p class="product-name product-name--hand" style="margin:0">Organic<br>Hand<br>Washes</p>
    <p class="product-note" style="margin:0">with natural pulp</p>
  </section>

  <section class="label label--rounded label--hand-wash-flat" aria-label="Hand wash label, flat">
    <div class="brand-band">
      <span class="brand-name">The Busy Wren</span>
      <span class="brand-tagline">Organic &amp; Natural Soaps</span>
    </div>
    <p class="product-name product-name--hand" style="margin:0">Organic<br>Hand<br>Washes</p>
    <p class="product-note" style="margin:0">with natural pulp</p>
  </section>

</main>
</body>
</html>
```